Diabetic test strips buying business needs business card

Hi all, thanks for picking up my project.

What we do is buy boxes of diabetic test strips from everyday people that are diabetics.

Many diabetes do not test all the time so they tend to have boxes left over.

This creates an opportunity for them to make some extra money by selling the boxes to us.

Here is some of the information i will want on the business card. We do not have a logo.

Name: Brandt / Dwayne
Toll Free : 1-800-555-0142

Call Today and Get Your Cash!

Website: www.glucoswapcorner.com
Email contact@glucoswapcorner.com

We buy diabetic test strips and pay you cash!
We accept many different brands.

Notes:

1 - Print should be readable since some diabetics have poor eyesight

2 - Sorry we do not have a logo

Please ask me any questions you have.

Thanks

Dwayne

I just increase the dollar amount on my business card project.

All, i'm going to decide on the design i think is the best for me today. Please don't submit anymore designs. Thank you all for your time and great designs. Dwayne

Diabetics

Business

• People i would like one sir of the card to be line a mini billboard. Seems like many of the design i'm seeing are very conservative as that my be my fault for not setting the slider bar correctly.

```html
<!DOCTYPE html>
<html lang="en">
<head>
<meta charset="utf-8">
<title>Glucoswap Corner business card</title>
<link rel="stylesheet" href="https://fonts.googleapis.com/css2?family=Questrial&family=Great+Vibes&display=swap">
<style>
  :root {
    --page: #ece8e3;
    --navy: #24215e;
    --navy-deep: #0b1057;
    --glow: #2a5aa8;
    --green: #8dc63f;
    --green-pale: #e9f3d9;
    --brand-green: #1d7a3b;
    --sky: #1e90d8;
    --sky-pale: #c4e6f8;
    --white: #ffffff;
  }
  * { margin: 0; padding: 0; box-sizing: border-box; }
  html, body { width: 1200px; height: 1000px; overflow: hidden; }
  body { background: var(--page); position: relative; font-family: "Questrial", sans-serif; }

  .card {
    position: absolute;
    left: 256px;
    width: 690px;
    height: 393px;
    overflow: hidden;
    box-shadow: 3px 4px 8px rgba(0,0,0,0.3);
  }
  .card--front { top: 74px; background: var(--navy); }
  .card--back { top: 507px; height: 394px; background: var(--navy-deep); color: var(--white); }

  .front-art { position: absolute; inset: 0; width: 100%; height: 100%; }

  .brand-name {
    position: absolute;
    left: 28px;
    top: 318px;
    font-size: 40px;
    color: var(--brand-green);
    letter-spacing: -0.5px;
  }

  .contact-top {
    position: absolute;
    left: 290px;
    top: 58px;
    font-size: 28px;
    line-height: 39px;
    font-weight: 700;
  }
  .tagline {
    position: absolute;
    left: 0;
    right: 0;
    top: 185px;
    text-align: center;
    font-family: "Great Vibes", cursive;
    font-size: 44px;
    color: var(--green);
  }
  .contact-bottom {
    position: absolute;
    left: 30px;
    top: 304px;
    font-size: 26px;
    line-height: 36px;
    font-weight: 700;
  }
</style>
</head>
<body>
  <section class="card card--front" aria-label="Card front">
    <svg class="front-art" viewBox="0 0 690 393" aria-hidden="true">
      <defs>
        <radialGradient id="navyGlow" cx="0.55" cy="0.1" r="0.45">
          <stop offset="0" stop-color="var(--glow)"/>
          <stop offset="1" stop-color="var(--navy)"/>
        </radialGradient>
        <linearGradient id="greenFade" x1="0" y1="0" x2="1" y2="0">
          <stop offset="0" stop-color="var(--green)"/>
          <stop offset="0.45" stop-color="var(--green)"/>
          <stop offset="1" stop-color="var(--green-pale)"/>
        </linearGradient>
        <linearGradient id="skyBand" x1="0" y1="0" x2="1" y2="0.4">
          <stop offset="0" stop-color="var(--sky)"/>
          <stop offset="1" stop-color="var(--sky-pale)"/>
        </linearGradient>
      </defs>
      <rect class="front-sky" width="690" height="393" fill="url(#navyGlow)"/>
      <path class="front-swoosh" d="M290,75 C440,92 580,180 690,238 L690,312 C590,232 440,112 290,75 Z" fill="url(#skyBand)"/>
      <path class="front-swoosh-line" d="M300,78 C450,100 590,195 690,262" fill="none" stroke="var(--sky)" stroke-width="3" opacity="0.6"/>
      <path class="front-hill" d="M0,38 C120,10 300,20 420,95 C540,170 630,280 690,393 L0,393 Z" fill="url(#greenFade)"/>
    </svg>
    <div class="brand-name">glucoswapcorner</div>
  </section>

  <section class="card card--back" aria-label="Card back">
    <div class="contact-top">
      <p class="contact-name">Name: Brandt / Dwayne</p>
      <p class="contact-phone">Toll Free : 1-800-555-0142</p>
    </div>
    <p class="tagline">Call Today and Get Your Cash!</p>
    <div class="contact-bottom">
      <p class="contact-web">Website: www.glucoswapcorner.com</p>
      <p class="contact-email">Email contact@glucoswapcorner.com</p>
    </div>
  </section>
</body>
</html>
```